PowerPoint Template Design for Management Consultancy

I need a PPT template for a new management consulting company. I want a modern look that uses dark blues and greys for divider slides, white content slides and a creative use of the logo in the slides. The supplied images are used on the website so I'd like to incorporate these into the theme

Target Market(s)

Management Consulting

Industry/Entity Type

Consulting

Font styles to use
Sans Serif

Colors
3277b5

Requirements
Must have
• Options for title slide, divider slides, content slides using the logo provided
Plain white content slides with creative use of logo
Color theme uses dark blues and greys
Nice to have
• Light and dark theme

```html
<!DOCTYPE html>
<html lang="en">
<head>
<meta charset="utf-8">
<title>Veralt Consulting – Presentation Template</title>
<link href="https://fonts.googleapis.com/css2?family=Lato:wght@300;400;700&display=swap" rel="stylesheet">
<style>
:root{
  --navy:#243a7c;
  --navy-deep:#1d2f66;
  --grey-dark:#48484d;
  --grey:#8b8d93;
  --grey-light:#d9dadd;
  --ink:#2a2c33;
  --body:#6d7079;
  --white:#ffffff;
  --paper:#ffffff;
}
*{margin:0;padding:0;box-sizing:border-box}
html,body{width:1200px;height:2400px;overflow:hidden;background:var(--paper);font-family:'Lato',Arial,sans-serif;color:var(--ink)}
.canvas{position:relative;width:1200px;height:2400px}
.brand-head{position:absolute;left:0;top:78px;width:1200px;text-align:center}
.brand-head .name{font-size:58px;font-weight:700;color:var(--navy);letter-spacing:6px;line-height:1}
.brand-head .rule{display:block;margin:14px auto 0;width:380px;height:3px;background:var(--grey-light)}

.slide{position:absolute;width:464px;height:262px;overflow:hidden;background:var(--white);box-shadow:0 3px 10px rgba(0,0,0,.28)}
.col-l{left:82px}.col-r{left:661px}
.r1{top:216px}.r2{top:527px}.r3{top:838px}.r4{top:1149px}.r5{top:1460px}.r6{top:1771px}.r7{top:2082px}

.abs{position:absolute}
.mark{position:absolute;top:16px;right:16px;width:11px;height:11px;border:2px solid var(--navy)}
.mark.light{border-color:var(--white)}
.foot-name{position:absolute;left:31px;bottom:6px;font-size:5.5px;font-weight:700;color:var(--navy);letter-spacing:.6px}
.foot-name.light{color:var(--white)}
.foot-url{position:absolute;left:208px;bottom:7px;font-size:3.4px;color:var(--body)}
.foot-num{position:absolute;right:31px;bottom:7px;font-size:3.4px;color:var(--body)}

.title{font-weight:300;font-size:20px;line-height:1.1;color:var(--ink);white-space:nowrap}
.title.light{color:var(--white)}
.sub{font-size:8px;font-weight:400;color:var(--body);margin-top:4px}
.sub.light{color:#e3e7f2}
.body{font-size:3.3px;line-height:1.42;color:var(--body);text-align:justify}
.body p{margin-bottom:3.5px}
.body.light{color:#dfe4f1}

.ph{position:absolute}
.ph-dusk{background:linear-gradient(180deg,#334f8c 0%,#5c6f99 35%,#b39a82 62%,#4a4f66 80%,#23283a 100%)}
.ph-haze{background:linear-gradient(180deg,#d8ccbf 0%,#9aa7bc 35%,#6a7fa0 65%,#3d4d6c 100%)}
.ph-sunset{background:radial-gradient(circle at 35% 40%,#fff2c8 0%,#f0c27a 12%,#8d97ad 40%,#3e5a92 70%,#1e2a40 100%)}
.ph-peak{background:linear-gradient(135deg,#a9b6c9 0%,#7f93b2 45%,#2b3142 72%,#15181f 100%)}

.grid{position:absolute;display:grid;gap:2px;background:var(--white)}
.grid .ph{position:static}

.bub{display:inline-flex;align-items:center;justify-content:center;border-radius:50%}
.bub svg{width:58%;height:58%}
.ico{width:12px;height:12px;color:var(--white)}

.toc-row{position:absolute;left:218px;width:206px;height:22.5px;border-bottom:.6px solid var(--grey-light);display:flex;align-items:center}
.toc-num{width:27px;font-size:11px;color:var(--ink)}
.toc-txt b{display:block;font-size:7px;font-weight:400;color:var(--ink)}
.toc-txt span{display:block;font-size:5.3px;color:var(--grey)}

.tile{position:relative;border:2px solid var(--grey-dark)}
.tile .cap{position:absolute;left:0;right:0;top:62%;text-align:center;font-size:3.6px;color:#eef0f5;padding:0 8px}
.tile .bub{position:absolute;left:50%;top:34%;transform:translate(-50%,-50%);width:20px;height:20px;border:1px solid #fff}

.item{position:absolute;display:flex;align-items:center;gap:9px}
.item .bub{width:19px;height:19px;flex:none}
.item b{display:block;font-size:5.5px;font-weight:400}
.item span{display:block;font-size:3.6px;line-height:1.4}

.stat{position:absolute;left:270px;width:194px;color:var(--white);text-align:center}
.stat b{display:block;font-size:13px;font-weight:400;margin-top:30px}
.stat span{display:block;font-size:3.4px;margin-top:4px;padding:0 50px;line-height:1.4}

.card{position:absolute;top:99px;width:92px;height:120px;background:#f2f3f6;border:.6px solid var(--grey-light);text-align:center}
.card .bub{margin-top:26px;width:22px;height:22px;background:var(--navy)}
.card b{display:block;font-size:4.6px;font-weight:400;color:var(--body);margin-top:10px}
.card span{display:block;font-size:3.4px;line-height:1.5;color:var(--grey);margin-top:8px;padding:0 10px}

.cell{position:absolute;color:var(--white);padding:8px 9px}
.cell .ico{display:block;margin:0 auto 8px;width:11px;height:11px}
.cell p{font-size:3.4px;line-height:1.45;text-align:justify}

.donut-box{position:absolute;left:269px;width:163px;color:var(--white)}
.donut-box svg{position:absolute;left:20px;top:12px;width:66px;height:66px}
.donut-box .val{position:absolute;left:92px;top:54px;font-size:7px}
.donut-box .val small{font-size:4px}
.donut-box .txt{position:absolute;left:92px;top:64px;width:64px;font-size:3.2px;line-height:1.45}
</style>
</head>
<body>
<svg width="0" height="0" style="position:absolute" aria-hidden="true">
  <defs>
    <symbol id="i-target" viewBox="0 0 24 24"><g fill="none" stroke="currentColor" stroke-width="2"><circle cx="12" cy="12" r="8"/><circle cx="12" cy="12" r="3.5"/><path d="M12 1v5M12 18v5M1 12h5M18 12h5"/></g></symbol>
    <symbol id="i-hour" viewBox="0 0 24 24"><g fill="none" stroke="currentColor" stroke-width="2"><path d="M5 2h14M5 22h14M7 2c0 6 10 7 10 10s-10 4-10 10M17 2c0 6-10 7-10 10s10 4 10 10"/></g></symbol>
    <symbol id="i-watch" viewBox="0 0 24 24"><g fill="none" stroke="currentColor" stroke-width="2"><circle cx="12" cy="14" r="8"/><path d="M12 14V9M9 2h6M12 2v4"/></g></symbol>
    <symbol id="i-gear" viewBox="0 0 24 24"><g fill="none" stroke="currentColor"><circle cx="12" cy="12" r="3" stroke-width="2"/><circle cx="12" cy="12" r="7.5" stroke-width="3.5" stroke-dasharray="3 2.9"/></g></symbol>
    <symbol id="i-pie" viewBox="0 0 24 24"><g fill="none" stroke="currentColor" stroke-width="2"><circle cx="12" cy="12" r="9"/><path d="M12 3v9h9"/></g></symbol>
    <symbol id="i-screen" viewBox="0 0 24 24"><g fill="none" stroke="currentColor" stroke-width="2"><rect x="3" y="4" width="18" height="12"/><path d="M12 16v4M8 20h8M9 10l2 2 4-4"/></g></symbol>
    <symbol id="i-team" viewBox="0 0 24 24"><g fill="none" stroke="currentColor" stroke-width="2"><circle cx="12" cy="8" r="3"/><circle cx="6" cy="15" r="3"/><circle cx="18" cy="15" r="3"/></g></symbol>
  </defs>
</svg>

<main class="canvas">
  <header class="brand-head">
    <div class="name">VERALT CONSULTING</div>
    <span class="rule"></span>
  </header>

  <!-- Row 1 -->
  <section class="slide col-l r1 slide-cover">
    <div class="ph ph-dusk" style="inset:0" role="img" aria-label="Two hikers with raised arms on a summit above misty mountains at dusk"></div>
    <div class="abs" style="left:238px;top:84px;width:190px;text-align:center">
      <div style="font-size:17px;font-weight:700;color:var(--navy);letter-spacing:1.5px">VERALT</div>
      <div style="font-size:9.5px;color:var(--white);margin-top:22px;letter-spacing:.3px">YOUR TITLE PRESENTATION HERE</div>
      <div style="font-size:7.5px;color:#eef0f5;margin-top:3px">Your subtitle presentation goes here</div>
    </div>
    <div class="foot-url" style="color:#dfe3ee">www.veraltconsulting.com</div>
    <div class="foot-num" style="color:#dfe3ee">1</div>
  </section>

  <section class="slide col-r r1 slide-contents">
    <div class="mark"></div>
    <div class="abs" style="left:29px;top:54px">
      <div class="title" style="font-size:22px;line-height:1.25">Investor<br>Presentation</div>
      <div style="font-size:7px;color:var(--body);letter-spacing:.3px;margin-top:1px">TABLE OF CONTENTS</div>
    </div>
    <div class="toc-row" style="top:52px"><span class="toc-num">01</span><div class="toc-txt"><b>Opportunity</b><span>Investment Highlights</span></div></div>
    <div class="toc-row" style="top:74.5px"><span class="toc-num">02</span><div class="toc-txt"><b>Property Overview</b><span>Property Description, Market Overview</span></div></div>
    <div class="toc-row" style="top:97px"><span class="toc-num">03</span><div class="toc-txt"><b>Market Overview</b><span>Submarket Overview &amp; Comparables</span></div></div>
    <div class="toc-row" style="top:119.5px"><span class="toc-num">04</span><div class="toc-txt"><b>Business Plan</b><span>Renovations, Timeline, Case Study</span></div></div>
    <div class="toc-row" style="top:142px"><span class="toc-num">05</span><div class="toc-txt"><b>Investment Structure</b><span>Summary of Terms, Sample Investment</span></div></div>
    <div class="toc-row" style="top:164.5px"><span class="toc-num">06</span><div class="toc-txt"><b>Harbor Lane Partners Overview</b><span>Strategy, Timeline, Principals, Process, Track Record</span></div></div>
    <div class="toc-row" style="top:187px"><span class="toc-num">07</span><div class="toc-txt"><b>Appendix</b><span>Representative Transactions</span></div></div>
    <div class="foot-name">VERALT</div><div class="foot-url">www.veraltconsulting.com</div><div class="foot-num">2</div>
  </section>

  <!-- Row 2 -->
  <section class="slide col-l r2">
    <div class="mark"></div>
    <div class="abs" style="left:31px;top:42px">
      <div class="title">Tour title slide here</div>
      <div class="sub">Your subtitle slide goges here</div>
    </div>
    <div class="abs body" style="left:31px;top:88px;width:200px;height:140px;overflow:hidden">
      <p>Our team studies each market closely, tests every plan with real data and shapes a clear path so partners can act with confidence and measure results over time.</p>
      <p>Our team studies each market closely, tests every plan with real data and shapes a clear path so partners can act with confidence and measure results over time. Our team studies each market closely, tests every plan with real data and shapes a clear path so partners can act with confidence and measure results over time.</p>
      <p>Our team studies each market closely, tests every plan with real data and shapes a clear path so partners can act with confidence and measure results over time.</p>
    </div>
    <div class="grid" style="left:247px;top:44px;width:186px;height:185px;grid-template-columns:1fr 1fr;grid-template-rows:1fr 1fr;gap:5px">
      <div class="tile ph ph-haze" role="img" aria-label="Hazy mountain ridges at sunrise"><span class="bub"><svg class="ico"><use href="#i-target"/></svg></span><div class="cap">Lorem ipsum dolor sit amet, consectetur adipiscing</div></div>
      <div class="tile ph ph-dusk" role="img" aria-label="Hikers celebrating on a summit"><span class="bub"><svg class="ico"><use href="#i-watch"/></svg></span><div class="cap">Lorem ipsum dolor sit amet, consectetur adipiscing</div></div>
      <div class="tile ph ph-dusk" role="img" aria-label="Hikers on a ridge at dusk"><span class="bub"><svg class="ico"><use href="#i-hour"/></svg></span><div class="cap">Lorem ipsum dolor sit amet, consectetur adipiscing</div></div>
      <div class="tile ph ph-peak" role="img" aria-label="Climber on a rocky peak"><span class="bub"><svg class="ico"><use href="#i-gear"/></svg></span><div class="cap">Lorem ipsum dolor sit amet, consectetur adipiscing</div></div>
    </div>
    <div class="foot-name">VERALT</div><div class="foot-url">www.veraltconsulting.com</div><div class="foot-num">4</div>
  </section>

  <section class="slide col-r r2">
    <div class="abs" style="left:270px;top:0;width:194px;height:262px;background:var(--navy)"></div>
    <div class="mark light"></div>
    <div class="abs" style="left:31px;top:38px">
      <div class="title">Tour title slide here</div>
      <div class="sub">Your subtitle slide goges here</div>
    </div>
    <div class="grid" style="left:31px;top:84px;width:223px;height:147px;grid-template-columns:1fr 1fr 1fr;grid-template-rows:1fr 1fr" role="img" aria-label="Hikers with raised arms on a summit against the setting sun, shown in six panels">
      <div class="ph ph-sunset"></div><div class="ph ph-sunset"></div><div class="ph ph-sunset"></div>
      <div class="ph ph-peak"></div><div class="ph ph-peak"></div><div class="ph ph-peak"></div>
    </div>
    <div class="abs body light" style="left:295px;top:44px;width:139px;height:44px;overflow:hidden">
      <p>Our team studies each market closely, tests every plan with real data and shapes a clear path so partners can act with confidence and measure results over time.</p>
    </div>
    <div class="item" style="left:295px;top:111px;color:var(--white)"><span class="bub" style="background:var(--white);color:var(--navy)"><svg><use href="#i-target"/></svg></span><div style="width:110px"><b>Lorem ipsum dolor sit amet</b><span>Quickly leverage other's distributed internal or "organic" sources rather than empowered materials.</span></div></div>
    <div class="item" style="left:295px;top:155px;color:var(--white)"><span class="bub" style="background:var(--white);color:var(--navy)"><svg><use href="#i-hour"/></svg></span><div style="width:110px"><b>Lorem ipsum dolor sit amet</b><span>Quickly leverage other's distributed internal or "organic" sources rather than empowered materials.</span></div></div>
    <div class="item" style="left:295px;top:199px;color:var(--white)"><span class="bub" style="background:var(--white);color:var(--navy)"><svg><use href="#i-watch"/></svg></span><div style="width:110px"><b>Lorem ipsum dolor sit amet</b><span>Quickly leverage other's distributed internal or "organic" sources rather than empowered materials.</span></div></div>
    <div class="foot-name">VERALT</div><div class="foot-url">www.veraltconsulting.com</div>
  </section>

  <!-- Row 3 -->
  <section class="slide col-l r3">
    <div class="ph ph-haze" style="inset:0" role="img" aria-label="Layered blue mountain ridges with a climber pulling a partner up a dark cliff"></div>
    <div class="abs" style="left:245px;top:110px;font-size:25px;font-weight:400;color:var(--white)">Breakslide</div>
  </section>

  <section class="slide col-r r3">
    <div class="abs" style="left:0;top:0;width:258px;height:262px;background:var(--navy)"></div>
    <div class="mark"></div>
    <div class="abs" style="left:31px;top:38px">
      <div class="title light">Tour title slide here</div>
      <div class="sub light">Your subtitle slide goges here</div>
    </div>
    <div class="abs body light" style="left:31px;top:86px;width:207px;height:140px;overflow:hidden">
      <p>Our team studies each market closely, tests every plan with real data and shapes a clear path so partners can act with confidence and measure results over time.</p>
      <p>Our team studies each market closely, tests every plan with real data and shapes a clear path so partners can act with confidence and measure results over time. Our team studies each market closely, tests every plan with real data and shapes a clear path so partners can act with confidence and measure results over time.</p>
      <p>Our team studies each market closely, tests every plan with real data and shapes a clear path so partners can act with confidence and measure results over time.</p>
    </div>
    <div class="ph ph-peak" style="left:268px;top:38px;width:164px;height:91px" role="img" aria-label="Climbers on a cliff above misty mountains"></div>
    <div class="ph ph-sunset" style="left:268px;top:142px;width:164px;height:91px" role="img" aria-label="Hikers with raised arms at sunset"></div>
    <div class="foot-name light">VERALT</div><div class="foot-num">6</div>
  </section>

  <!-- Row 4 -->
  <section class="slide col-l r4">
    <div class="ph ph-dusk" style="left:0;top:0;width:95px;height:262px" role="img" aria-label="Two hikers with raised arms on a summit"></div>
    <div class="abs" style="left:95px;top:0;width:120px;height:262px;background:var(--navy)"></div>
    <div class="mark"></div>
    <div class="item" style="left:124px;top:44px;color:var(--white)"><span class="bub" style="background:var(--white);color:var(--navy)"><svg><use href="#i-target"/></svg></span><span style="width:55px">Lorem ipsum dolorm turu det et et alurun</span></div>
    <div class="item" style="left:124px;top:96px;color:var(--white)"><span class="bub" style="background:var(--white);color:var(--navy)"><svg><use href="#i-hour"/></svg></span><span style="width:55px">Lorem ipsum dolorm turu det et et alurun</span></div>
    <div class="item" style="left:124px;top:151px;color:var(--white)"><span class="bub" style="background:var(--white);color:var(--navy)"><svg><use href="#i-watch"/></svg></span><span style="width:55px">Lorem ipsum dolorm turu det et et alurun</span></div>
    <div class="item" style="left:124px;top:207px;color:var(--white)"><span class="bub" style="background:var(--white);color:var(--navy)"><svg><use href="#i-gear"/></svg></span><span style="width:55px">Lorem ipsum dolorm turu det et et alurun</span></div>
    <div class="abs" style="left:234px;top:46px">
      <div class="title">Tour title slide here</div>
      <div class="sub">Your subtitle slide goges here</div>
    </div>
    <div class="abs body" style="left:234px;top:98px;width:200px;height:128px;overflow:hidden">
      <p>Our team studies each market closely, tests every plan with real data and shapes a clear path so partners can act with confidence and measure results over time.</p>
      <p>Our team studies each market closely, tests every plan with real data and shapes a clear path so partners can act with confidence and measure results over time. Our team studies each market closely, tests every plan with real data and shapes a clear path so partners can act with confidence and measure results over time.</p>
      <p>Our team studies each market closely, tests every plan with real data and shapes a clear path so partners can act with confidence and measure results over time.</p>
    </div>
    <div class="foot-num">10</div>
  </section>

  <section class="slide col-r r4">
    <div class="stat" style="top:0;height:84px;background:var(--grey-dark)"><b>35,5%</b><span>Quickly leverage other's distributed internal or "organic" sources rather than empowered materials.</span></div>
    <div class="stat" style="top:89px;height:84px;background:var(--navy)"><b>95,8%</b><span>Quickly leverage other's distributed internal or "organic" sources rather than empowered materials.</span></div>
    <div class="stat" style="top:177px;height:85px;background:var(--grey-dark)"><b>56,4%</b><span>Quickly leverage other's distributed internal or "organic" sources rather than empowered materials.</span></div>
    <div class="abs" style="left:29px;top:34px">
      <div class="title">Tour title slide here</div>
      <div class="sub">Your subtitle slide goges here</div>
    </div>
    <div class="abs body" style="left:31px;top:84px;width:207px;height:28px;overflow:hidden">
      <p>Our team studies each market closely, tests every plan with real data and shapes a clear path so partners can act with confidence and measure results over time.</p>
    </div>
    <div class="item" style="left:69px;top:131px;color:var(--body)"><span class="bub" style="border:1.2px solid var(--navy);color:var(--navy)"><svg><use href="#i-target"/></svg></span><div style="width:120px"><b>Lorem ipsum dolor sit amet</b><span>Quickly leverage other's distributed internal or "organic" sources rather than empowered materials.</span></div></div>
    <div class="item" style="left:69px;top:168px;color:var(--body)"><span class="bub" style="border:1.2px solid var(--navy);color:var(--navy)"><svg><use href="#i-hour"/></svg></span><div style="width:120px"><b>Lorem ipsum dolor sit amet</b><span>Quickly leverage other's distributed internal or "organic" sources rather than empowered materials.</span></div></div>
    <div class="item" style="left:69px;top:205px;color:var(--body)"><span class="bub" style="border:1.2px solid var(--navy);color:var(--navy)"><svg><use href="#i-watch"/></svg></span><div style="width:120px"><b>Lorem ipsum dolor sit amet</b><span>Quickly leverage other's distributed internal or "organic" sources rather than empowered materials.</span></div></div>
    <div class="foot-name">VERALT</div><div class="foot-url">www.veraltconsulting.com</div>
  </section>

  <!-- Row 5 -->
  <section class="slide col-l r5">
    <div class="mark"></div>
    <div class="abs" style="left:31px;top:36px">
      <div class="title" style="font-size:22px;line-height:1.3">Title slide<br>goes here</div>
      <div class="sub">Your subtitle slide here</div>
    </div>
    <div class="abs body" style="left:147px;top:38px;width:286px;height:190px;overflow:hidden;font-size:3px">
      <p>Our team studies each market closely, tests every plan with real data and shapes a clear path so partners can act with confidence and measure results over time. Our team studies each market closely, tests every plan with real data and shapes a clear path so partners can act with confidence and measure results over time.</p>
      <p>Our team studies each market closely, tests every plan with real data and shapes a clear path so partners can act with confidence and measure results over time. Our team studies each market closely, tests every plan with real data and shapes a clear path so partners can act with confidence and measure results over time.</p>
      <p>Our team studies each market closely, tests every plan with real data and shapes a clear path so partners can act with confidence and measure results over time. Our team studies each market closely, tests every plan with real data and shapes a clear path so partners can act with confidence and measure results over time.</p>
      <p>Our team studies each market closely, tests every plan with real data and shapes a clear path so partners can act with confidence and measure results over time. Our team studies each market closely, tests every plan with real data and shapes a clear path so partners can act with confidence and measure results over time.</p>
    </div>
    <div class="foot-name">VERALT</div><div class="foot-url">www.veraltconsulting.com</div><div class="foot-num">6</div>
  </section>

  <section class="slide col-r r5">
    <div class="mark"></div>
    <div class="abs" style="left:31px;top:36px">
      <div class="title" style="font-size:22px;line-height:1.3">Title slide<br>goes here</div>
      <div class="sub">Your subtitle slide here</div>
    </div>
    <div class="abs body" style="left:146px;top:38px;width:140px;height:190px;overflow:hidden;font-size:3px">
      <p>Our team studies each market closely, tests every plan with real data and shapes a clear path so partners can act with confidence and measure results over time. Our team studies each market closely, tests every plan with real data and shapes a clear path so partners can act with confidence and measure results over time.</p>
      <p>Our team studies each market closely, tests every plan with real data and shapes a clear path so partners can act with confidence and measure results over time. Our team studies each market closely, tests every plan with real data and shapes a clear path so partners can act with confidence and measure results over time.</p>
      <p>Our team studies each market closely, tests every plan with real data and shapes a clear path so partners can act with confidence and measure results over time. Our team studies each market closely, tests every plan with real data and shapes a clear path so partners can act with confidence and measure results over time.</p>
    </div>
    <div class="abs body" style="left:294px;top:38px;width:139px;height:160px;overflow:hidden;font-size:3px">
      <p>Our team studies each market closely, tests every plan with real data and shapes a clear path so partners can act with confidence and measure results over time. Our team studies each market closely, tests every plan with real data and shapes a clear path so partners can act with confidence and measure results over time.</p>
      <p>Our team studies each market closely, tests every plan with real data and shapes a clear path so partners can act with confidence and measure results over time. Our team studies each market closely, tests every plan with real data and shapes a clear path so partners can act with confidence and measure results over time.</p>
      <p>Our team studies each market closely, tests every plan with real data and shapes a clear path so partners can act with confidence and measure results over time. Our team studies each market closely, tests every plan with real data and shapes a clear path so partners can act with confidence and measure results over time.</p>
    </div>
    <div class="foot-name">VERALT</div><div class="foot-url">www.veraltconsulting.com</div><div class="foot-num">7</div>
  </section>

  <!-- Row 6 -->
  <section class="slide col-l r6">
    <div class="mark"></div>
    <div class="grid" style="left:32px;top:44px;width:185px;height:186px;grid-template-columns:1fr 1fr 1fr;grid-template-rows:1fr 1fr 1fr" role="img" aria-label="Hikers with raised arms against a bright sunset, shown in nine panels">
      <div class="ph ph-sunset"></div><div class="ph ph-haze"></div><div class="ph ph-dusk"></div>
      <div class="ph ph-sunset"></div><div class="ph ph-dusk"></div><div class="ph ph-dusk"></div>
      <div class="ph ph-peak"></div><div class="ph ph-peak"></div><div class="ph ph-peak"></div>
    </div>
    <div class="abs" style="left:234px;top:46px">
      <div class="title">Tour title slide here</div>
      <div class="sub">Your subtitle slide goges here</div>
    </div>
    <div class="abs body" style="left:234px;top:98px;width:200px;height:128px;overflow:hidden">
      <p>Our team studies each market closely, tests every plan with real data and shapes a clear path so partners can act with confidence and measure results over time.</p>
      <p>Our team studies each market closely, tests every plan with real data and shapes a clear path so partners can act with confidence and measure results over time. Our team studies each market closely, tests every plan with real data and shapes a clear path so partners can act with confidence and measure results over time.</p>
      <p>Our team studies each market closely, tests every plan with real data and shapes a clear path so partners can act with confidence and measure results over time.</p>
    </div>
    <div class="foot-name">VERALT</div><div class="foot-url">www.veraltconsulting.com</div><div class="foot-num">12</div>
  </section>

  <section class="slide col-r r6">
    <div class="ph" style="left:0;top:0;width:464px;height:121px;background:linear-gradient(180deg,var(--navy-deep),var(--navy) 60%,#3a4f8c)" role="img" aria-label="Faint silhouettes of hikers on a summit over a navy band"></div>
    <div class="mark light"></div>
    <div class="abs" style="left:31px;top:32px">
      <div class="title light">Tour title slide here</div>
      <div class="sub light">Your subtitle slide goges here</div>
    </div>
    <div class="card" style="left:31px"><span class="bub"><svg class="ico"><use href="#i-target"/></svg></span><b>Your title here</b><span>Quickly leverage other's distributed internal or "organic" sources rather than empowered materials. Conveniently leverage existing client-centric.</span></div>
    <div class="card" style="left:134px"><span class="bub"><svg class="ico"><use href="#i-team"/></svg></span><b>Your title here</b><span>Quickly leverage other's distributed internal or "organic" sources rather than empowered materials. Conveniently leverage existing client-centric.</span></div>
    <div class="card" style="left:237px"><span class="bub"><svg class="ico"><use href="#i-pie"/></svg></span><b>Your title here</b><span>Quickly leverage other's distributed internal or "organic" sources rather than empowered materials. Conveniently leverage existing client-centric.</span></div>
    <div class="card" style="left:340px"><span class="bub"><svg class="ico"><use href="#i-screen"/></svg></span><b>Your title here</b><span>Quickly leverage other's distributed internal or "organic" sources rather than empowered materials. Conveniently leverage existing client-centric.</span></div>
    <div class="foot-name">VERALT</div><div class="foot-url">www.veraltconsulting.com</div><div class="foot-num">13</div>
  </section>

  <!-- Row 7 -->
  <section class="slide col-l r7">
    <div class="mark"></div>
    <div class="ph ph-haze" style="left:32px;top:44px;width:101px;height:185px" role="img" aria-label="Misty mountain layers at sunrise"></div>
    <div class="cell" style="left:133px;top:44px;width:99px;height:185px;background:var(--navy);padding:10px 10px">
      <div style="font-size:12px;font-weight:300;line-height:1.2">Tour title<br>slide here</div>
      <div style="font-size:8px;line-height:1.2;margin:10px 0 6px">Your subtitle<br>slide goes here</div>
      <p>Our team studies each market closely, tests every plan with real data and shapes a clear path so partners can act with confidence and measure results over time.</p>
    </div>
    <div class="cell" style="left:232px;top:44px;width:101px;height:92px;background:var(--navy)"><svg class="ico"><use href="#i-watch"/></svg><p>"Sed ut perspiciatis unde omnis iste natus error sit voluptatem accusantium doloremque laudantium, totam rem aperiam, eaque ipsa quae ab illo inventore veritatis et quasi architecto beatae vitae dicta sunt explicabo.</p></div>
    <div class="cell" style="left:333px;top:44px;width:100px;height:92px;background:var(--grey-dark)"><svg class="ico"><use href="#i-gear"/></svg><p>"Sed ut perspiciatis unde omnis iste natus error sit voluptatem accusantium doloremque laudantium, totam rem aperiam, eaque ipsa quae ab illo inventore veritatis et quasi architecto beatae vitae dicta sunt explicabo.</p></div>
    <div class="cell" style="left:232px;top:137px;width:101px;height:92px;background:var(--grey-dark)"><svg class="ico"><use href="#i-hour"/></svg><p>"Sed ut perspiciatis unde omnis iste natus error sit voluptatem accusantium doloremque laudantium, totam rem aperiam, eaque ipsa quae ab illo inventore veritatis et quasi architecto beatae vitae dicta sunt explicabo.</p></div>
    <div class="cell" style="left:333px;top:137px;width:100px;height:92px;background:var(--navy)"><svg class="ico"><use href="#i-target"/></svg><p>"Sed ut perspiciatis unde omnis iste natus error sit voluptatem accusantium doloremque laudantium, totam rem aperiam, eaque ipsa quae ab illo inventore veritatis et quasi architecto beatae vitae dicta sunt explicabo.</p></div>
    <div class="foot-name">VERALT</div><div class="foot-url">www.veraltconsulting.com</div><div class="foot-num">14</div>
  </section>

  <section class="slide col-r r7">
    <div class="mark"></div>
    <div class="abs" style="left:0;top:44px;width:262px;height:185px;background:var(--navy)"></div>
    <div class="abs" style="left:33px;top:66px">
      <div class="title light">Tour title slide here</div>
      <div class="sub light">Your subtitle slide goges here</div>
    </div>
    <div class="abs body light" style="left:33px;top:110px;width:210px;height:112px;overflow:hidden">
      <p>Our team studies each market closely, tests every plan with real data and shapes a clear path so partners can act with confidence and measure results over time.</p>
      <p>Our team studies each market closely, tests every plan with real data and shapes a clear path so partners can act with confidence and measure results over time. Our team studies each market closely, tests every plan with real data and shapes a clear path so partners can act with confidence and measure results over time.</p>
      <p>Our team studies each market closely, tests every plan with real data and shapes a clear path so partners can act with confidence and measure results over time.</p>
    </div>
    <div class="donut-box" style="top:44px;height:92px;background:var(--grey-dark)">
      <svg viewBox="0 0 66 66"><circle cx="33" cy="33" r="24" fill="none" stroke="#6c6d73" stroke-width="7"/><circle cx="33" cy="33" r="24" fill="none" stroke="var(--grey-light)" stroke-width="7" stroke-dasharray="128.2 150.8" transform="rotate(-90 33 33)"/></svg>
      <div class="val">85<small>%</small></div>
      <div class="txt">Quickly leverage other's distributed internal or "organic" sources. Business Inside</div>
    </div>
    <div class="donut-box" style="top:138px;height:91px;background:var(--navy)">
      <svg viewBox="0 0 66 66"><circle cx="33" cy="33" r="24" fill="none" stroke="#4d66a8" stroke-width="7"/><circle cx="33" cy="33" r="24" fill="none" stroke="var(--navy-deep)" stroke-width="7" stroke-dasharray="105.6 150.8" transform="rotate(-90 33 33)"/></svg>
      <div class="val">70<small>%</small></div>
      <div class="txt">Quickly leverage other's distributed internal or "organic" sources. Business Inside</div>
    </div>
    <div class="foot-name">VERALT</div><div class="foot-url">www.veraltconsulting.com</div><div class="foot-num">15</div>
  </section>
</main>
</body>
</html>
```